Verdant Holdings Scholarship

Looking to make an attractive scholarship description graphic for my website. Please use the text on the word doc and integrate the two graphics into the layout. Here's what I am looking to replace with the winning design: https://qmeadowllc.example/scholarship-contest/

Thank you

```html
<!DOCTYPE html>
<html lang="en">
<head>
<meta charset="utf-8">
<title>Verdant Holdings Scholarship</title>
<link href="https://fonts.googleapis.com/css2?family=Roboto+Condensed:wght@400;700&display=swap" rel="stylesheet">
<style>
  :root {
    --purple: #5b2e86;
    --purple-deep: #35204f;
    --purple-ink: #2c1a44;
    --gold: #d6bd3f;
    --gold-soft: #e2cd5a;
    --paper: #ffffff;
    --mist: #ecebef;
    --text: #2a1d3c;
  }
  html, body { margin: 0; padding: 0; }
  body {
    width: 1200px; height: 2824px; overflow: hidden; position: relative;
    background: var(--paper);
    font-family: "Roboto Condensed", "Arial Narrow", sans-serif;
    color: var(--text);
  }
  .abs { position: absolute; }

  .header { left: 0; top: 0; width: 1200px; height: 604px;
    background: linear-gradient(180deg, #f4f4f6 0%, var(--mist) 100%); }
  .hero-photo { left: 440px; top: 0; width: 760px; height: 604px;
    background: radial-gradient(ellipse at 55% 60%, #3a3440 0%, #cfcbd2 55%, #eeeef1 100%); }
  .brand { left: 90px; top: 200px; display: flex; align-items: center; gap: 18px; }
  .brand-mark { width: 44px; height: 44px; background: var(--purple); }
  .brand-name { font-size: 46px; font-weight: 400; color: var(--purple); line-height: 1; }
  .purpose-kicker { left: 113px; top: 482px; font-size: 30px; color: var(--purple); }
  .purpose-title { left: 113px; top: 525px; font-size: 56px; color: var(--purple); }

  .gold-band { left: 0; top: 604px; width: 1200px; height: 113px; background: var(--gold); }
  .purpose-panel { left: 86px; top: 604px; width: 498px; height: 369px; background: var(--purple);
    box-sizing: border-box; padding: 18px 28px 0 20px; }
  .purpose-item { display: flex; gap: 12px; font-size: 25px; line-height: 1.33; color: #fff;
    padding: 12px 0 14px; border-bottom: 1px solid rgba(255,255,255,0.18); }
  .purpose-item:last-child { border-bottom: 0; }
  .dot { flex: none; width: 18px; height: 18px; border-radius: 50%; background: var(--gold); margin-top: 8px; }

  .application { left: 86px; top: 973px; width: 498px; height: 235px; background: var(--purple-deep); }
  .application h2 { position: absolute; left: 22px; top: 20px; margin: 0; font-weight: 400; font-size: 45px; color: #fff; }
  .application p { position: absolute; left: 188px; top: 80px; margin: 0; width: 300px;
    font-size: 21px; line-height: 1.3; color: #fff; }
  .application svg { position: absolute; left: 30px; top: 84px; }

  .eligibility-head { left: 584px; top: 604px; width: 616px; height: 113px; display: flex; align-items: center; gap: 20px;
    box-sizing: border-box; padding-left: 26px; }
  .eligibility-head h3 { margin: 0; font-size: 25px; line-height: 1.3; font-weight: 700; color: var(--purple-ink); }
  .eligibility-list { left: 584px; top: 717px; width: 616px; height: 491px; background: var(--paper); }
  .req { position: absolute; left: 26px; display: flex; gap: 22px; align-items: flex-start; }
  .req p { margin: 0; font-size: 25px; line-height: 1.32; color: var(--purple-ink); width: 440px; }

  .package { left: 0; top: 1208px; width: 1200px; height: 670px; background: var(--purple-deep); }
  .email-pill { left: 94px; top: 1233px; width: 1012px; height: 53px; border-radius: 27px; background: var(--gold);
    display: flex; align-items: center; box-sizing: border-box; padding-left: 64px; gap: 20px;
    font-size: 31px; color: var(--purple-ink); }
  .pointer { left: 272px; top: 1196px; }
  .package-title { left: 165px; top: 1326px; font-size: 27px; color: #fff; }
  .check-row { position: absolute; left: 295px; display: flex; gap: 14px; color: var(--gold-soft); font-size: 25px; line-height: 1.33; }
  .check-row small { display: block; font-size: 17px; line-height: 1.3; }
  .pkg-icon { position: absolute; left: 160px; }

  .info { left: 0; width: 1200px; }
  .info .tab { position: absolute; left: 0; top: 18px; width: 142px; height: 36px; background: var(--purple-deep);
    border-radius: 0 18px 18px 0; }
  .info .tab::after { content: ""; position: absolute; right: 4px; top: 3px; width: 30px; height: 30px;
    border-radius: 50%; background: var(--gold); }
  .info h2 { margin: 0 0 0 166px; font-size: 48px; font-weight: 400; line-height: 1.2; color: var(--purple-ink); }
  .info p { margin: 0 0 0 166px; width: 930px; font-size: 26px; line-height: 1.36; color: var(--purple-ink); }

  .footer { left: 0; top: 2719px; width: 1200px; height: 105px; background: var(--purple-deep);
    display: flex; align-items: center; justify-content: center;
    font-size: 29px; letter-spacing: 15px; color: #fff; }
</style>
</head>
<body>
  <div class="abs header"></div>
  <div class="abs hero-photo" role="img" aria-label="Photo of three smiling high school graduates in caps and gowns holding diplomas tied with red ribbon"></div>
  <div class="abs brand"><span class="brand-mark"></span><span class="brand-name">Verdant Holdings</span></div>
  <div class="abs purpose-kicker">Purpose of this</div>
  <div class="abs purpose-title">Scholarship:</div>

  <div class="abs gold-band"></div>
  <div class="abs purpose-panel">
    <div class="purpose-item"><span class="dot"></span><span>To increase trade school, college, and university opportunities of high school seniors</span></div>
    <div class="purpose-item"><span class="dot"></span><span>To encourage high academic achievement in our youth</span></div>
    <div class="purpose-item"><span class="dot"></span><span>To reward hard-working high school seniors and assist in collegiate expenses</span></div>
  </div>

  <div class="abs application">
    <h2>Application:</h2>
    <svg width="140" height="130" viewBox="0 0 140 130" fill="none" stroke="#d6bd3f" stroke-width="4">
      <rect x="4" y="28" width="104" height="72" rx="4"/>
      <rect x="16" y="18" width="104" height="72" rx="4"/>
      <circle cx="60" cy="58" r="18"/><path d="M54 48 L70 58 L54 68 Z"/>
      <path d="M40 100 L34 118 H80 L74 100"/>
      <path d="M94 10 L118 2 L138 12 L118 22 Z"/><path d="M104 16 V26 H130 V16"/>
    </svg>
    <p>The application can be submitted via upload on this website, mail (see mailing address below), or scan &amp; email.</p>
  </div>

  <div class="abs eligibility-head">
    <svg width="70" height="80" viewBox="0 0 70 80" fill="none" stroke="#2c1a44" stroke-width="3.5">
      <circle cx="35" cy="48" r="28"/><ellipse cx="35" cy="48" rx="12" ry="28"/>
      <path d="M7 48 H63 M12 34 H58 M12 62 H58"/>
      <path d="M8 14 L35 2 L62 14 L35 26 Z"/>
    </svg>
    <h3>Eligibility and Requirements at the<br>time of submission for this scholarship:</h3>
  </div>
  <div class="abs eligibility-list">
    <div class="req" style="top:44px">
      <svg width="64" height="60" viewBox="0 0 64 60" fill="none" stroke="#5b2e86" stroke-width="3"><circle cx="22" cy="16" r="9"/><path d="M6 56 V40 Q22 26 38 40 V56 Z"/><rect x="34" y="26" width="26" height="22"/><path d="M40 34 H54 M40 40 H50"/></svg>
      <p>Applicant must be an enrolled high school student in his/her senior year</p>
    </div>
    <div class="req" style="top:143px">
      <svg width="64" height="70" viewBox="0 0 64 70" fill="none" stroke="#5b2e86" stroke-width="3"><circle cx="32" cy="8" r="6"/><path d="M18 18 L32 24 L46 18 M32 24 V40 M24 50 L32 40 L40 50"/><path d="M10 52 H54 V60 H10 Z M4 60 H60 V68 H4 Z"/></svg>
      <p>Applicant must be in good standing with their high school</p>
    </div>
    <div class="req" style="top:242px">
      <svg width="64" height="64" viewBox="0 0 64 64" fill="none" stroke="#5b2e86" stroke-width="3"><rect x="4" y="6" width="56" height="52" rx="3"/><path d="M12 16 H40 M12 26 H52 M12 36 H30"/><circle cx="46" cy="44" r="8"/><path d="M42 52 L40 62 M50 52 L52 62"/></svg>
      <p>Applicant must have a cumulative grade point average of at least 2.5 on a 4.0 scale</p>
    </div>
    <div class="req" style="top:374px">
      <svg width="64" height="64" viewBox="0 0 64 64" fill="none" stroke="#5b2e86" stroke-width="3"><rect x="4" y="6" width="14" height="12"/><rect x="4" y="26" width="14" height="12"/><rect x="4" y="46" width="14" height="12"/><path d="M7 12 L10 15 L16 8 M7 32 L10 35 L16 28 M7 52 L10 55 L16 48"/><circle cx="42" cy="12" r="7"/><path d="M32 62 V28 H52 V62 M42 40 V62"/></svg>
      <p>Applicant must be accepted to a 4-year accredited college, university, trade school or community college</p>
    </div>
  </div>

  <div class="abs package"></div>
  <svg class="abs pointer" width="28" height="40" viewBox="0 0 28 40"><path d="M14 0 L28 40 H0 Z" fill="#d6bd3f"/></svg>
  <div class="abs email-pill">Email address: jordanmeadow@qmeadowllc.example.
    <svg width="32" height="36" viewBox="0 0 32 36"><path d="M2 2 L28 20 L17 21 L23 33 L19 35 L13 23 L5 30 Z" fill="#2c1a44"/></svg>
  </div>
  <div class="abs package-title">The Application package must include:</div>

  <svg class="pkg-icon" style="top:1414px" width="104" height="102" viewBox="0 0 104 102" fill="none" stroke="#d6bd3f" stroke-width="3.5"><rect x="3" y="3" width="96" height="94"/><path d="M3 16 H99 M84 6 L94 14 M94 6 L84 14 M14 32 H70 M14 44 H86"/><rect x="14" y="54" width="64" height="16" rx="8"/><path d="M60 62 L76 90 L72 78 L84 80 Z M14 82 H50"/></svg>
  <svg class="pkg-icon" style="top:1552px" width="104" height="104" viewBox="0 0 104 104" fill="none" stroke="#d6bd3f" stroke-width="3.5"><path d="M6 4 H74 V96 H6 Z"/><path d="M16 20 H56 M16 32 H60 M16 44 H44 M16 56 H36"/><path d="M90 24 L98 32 L58 80 L46 86 L50 72 Z"/><path d="M80 90 L88 98 M92 86 L96 90"/></svg>
  <svg class="pkg-icon" style="top:1700px" width="110" height="112" viewBox="0 0 110 112" fill="none" stroke="#d6bd3f" stroke-width="3.5"><rect x="4" y="24" width="102" height="64" rx="3"/><path d="M40 88 L34 106 H76 L70 88"/><path d="M28 4 H82 V76 H28 Z"/><path d="M38 16 H72 M38 26 H72 M38 36 H60 M38 46 H72 M38 56 H66"/></svg>

  <svg width="0" height="0" style="position:absolute"><defs><path id="tick" d="M2 14 L10 22 L28 2" fill="none" stroke="#d6bd3f" stroke-width="5" stroke-linecap="round" stroke-linejoin="round"/></defs></svg>
  <div class="check-row" style="top:1419px"><svg width="30" height="26"><use href="#tick"/></svg><span>Completed application form</span></div>
  <div class="check-row" style="top:1484px"><svg width="30" height="26"><use href="#tick"/></svg><span>1 completed scholarship recommendation<small>(teacher, guidance counselor, coach, employer, clergy, NOT friends or family)</small></span></div>
  <div class="check-row" style="top:1577px"><svg width="30" height="26"><use href="#tick"/></svg><span>1 Essay no more than 2 pages in length, Times New Roman font<br>(size 12), 1” margins, &amp; double-spaced</span></div>
  <div class="check-row" style="top:1676px"><svg width="30" height="26"><use href="#tick"/></svg><span>Current high school transcript</span></div>
  <div class="check-row" style="top:1742px"><svg width="30" height="26"><use href="#tick"/></svg><span>A copy of a College, University, Trade School or Community College<br>acceptance letter</span></div>

  <section class="abs info" style="top:1936px">
    <span class="tab"></span>
    <h2>Scoring:</h2>
    <p>The Verdant Holdings Scholarship Scoring Committee will evaluate each application and select ONE winner. If there is a tie, the prize money will be split. The winning essay will be scored based on the grading rubric<br>(Rubric is in downloadable scholarship application packet).</p>
  </section>
  <section class="abs info" style="top:2170px">
    <span class="tab"></span>
    <h2>Scholarship Amount:</h2>
    <p>The Verdant Holdings Scholarship will award a minimum of $1,500.00 to the winning applicant. Payment will be to the institution that the winner will attend in the fall.</p>
  </section>
  <section class="abs info" style="top:2371px">
    <span class="tab"></span>
    <h2>Deadline:</h2>
    <p>The contest begins on 1 March. Applications postmarked, uploaded, and emailed after 31 May will not be accepted and returned to sender. Verdant Holdings will announce the winner no later than 1 August.</p>
  </section>
  <section class="abs info" style="top:2570px">
    <span class="tab"></span>
    <h2>Essay Topic:</h2>
    <p>The essay topic is posted on the last day of February</p>
  </section>

  <footer class="abs footer">www.qmeadowllc.example</footer>
</body>
</html>
```